Gifts for Truck Drivers Graphic Design

We are looking for a new design for a graphic to be used in a Christmas campaign called "Gifts for Truck Drivers." Gifts For Truck Drivers should be the main text of this graphic and other visuals can be used to support the theme. This will be promoted during Christmas, so traditional Christmas colors of red and green can be used.

We are going to have several different categories of gifts, but wish to start with just 1 general logo design that could be modified per each category. To be specific, we need to start with 1 main graphic that could then have different variations such as:

Gifts for Truck Drivers - Electronics
Gifts for Truck Drivers - Stocking Stuffers.

So while the main Gifts for Truck Drivers part of the graphic would remain the same, there could be 1 element that changes per each category to show what we are featuring.

Use of graphic - these graphics will be used online to drive traffic to our website, blog posts, etc. We request that the .psd be provided so we can resize for Facebook and other social promotions.

The main Call to Action or CTA for a button to go along with this graphic could be - show me gifts! The graphic will ultimately drive people to a list of gifts in each category.

The name of our company is The Copper Lantern. Our logo can be used subtly in the design if you see fit, but the main focus should be Gifts for Truck Drivers. Example: it could be used really small at the bottom to say - list brought to you by The Copper Lantern.

Target Market(s)

The target market is truck drivers typically around 35-55 as well as their friends and family who will be buying gifts.

Industry/Entity Type

Electronics

Requirements
Must have
• Must draw attention to Gifts for Truck Drivers
Must have a Christmas type theme
Must be easily adapted for different categories of gifts such as electronics and stocking stuffers

```html
<!DOCTYPE html>
<html lang="en">
<head>
<meta charset="UTF-8">
<title>Gifts for Truck Drivers</title>
<link rel="stylesheet" href="https://fonts.googleapis.com/css2?family=Great+Vibes&family=Alfa+Slab+One&family=Roboto+Condensed:wght@700&display=swap">
<style>
  :root {
    --backdrop: #000000;
    --card: #ffffff;
    --holly-green: #1f8a3a;
    --holly-green-dark: #146b2b;
    --berry-red: #c8151b;
    --ribbon-gold: #e2b43a;
    --box-red: #d42a22;
    --stocking-green: #3bb34a;
    --tag-paper: #f4e3d0;
  }
  * { margin: 0; padding: 0; box-sizing: border-box; }
  html, body {
    width: 898px;
    height: 1200px;
    overflow: hidden;
    background: var(--backdrop);
  }
  .canvas {
    position: relative;
    width: 898px;
    height: 1200px;
    background: var(--backdrop);
  }
  .category-card {
    position: absolute;
    left: 30px;
    width: 838px;
    height: 555px;
    background: var(--card);
    overflow: hidden;
  }
  .category-card--electronics { top: 30px; }
  .category-card--stockings { top: 615px; }

  .gift-artwork {
    position: absolute;
    left: 470px;
    top: 15px;
    width: 340px;
    height: 300px;
    border-radius: 12px;
  }
  .category-card--electronics .gift-artwork {
    background: radial-gradient(ellipse at 55% 65%, var(--box-red) 0%, #e05a4c 45%, #f3d7b0 80%, rgba(255,255,255,0) 100%);
  }
  .category-card--stockings .gift-artwork {
    background: radial-gradient(ellipse at 55% 65%, var(--box-red) 0%, #e46452 40%, #b9e0b8 75%, rgba(255,255,255,0) 100%);
  }

  .category-tag {
    position: absolute;
    left: 640px;
    top: 190px;
    width: 92px;
    height: 120px;
    background: var(--tag-paper);
    border: 2px solid #c9a98a;
    border-radius: 6px;
    transform: rotate(-22deg);
    display: flex;
    align-items: center;
    justify-content: center;
  }
  .category-tag span {
    writing-mode: vertical-rl;
    transform: rotate(180deg);
    font-family: "Roboto Condensed", sans-serif;
    font-weight: 700;
    font-size: 17px;
    color: var(--berry-red);
  }
  .category-tag::before {
    content: "";
    position: absolute;
    top: 10px;
    left: 50%;
    width: 12px;
    height: 12px;
    margin-left: -6px;
    border-radius: 50%;
    background: var(--card);
    border: 2px solid #c9a98a;
  }

  .campaign-title {
    position: absolute;
    left: 0;
    top: 0;
    width: 838px;
    height: 555px;
  }
  .title-gifts {
    position: absolute;
    left: 50px;
    top: 110px;
    font-family: "Great Vibes", cursive;
    font-size: 230px;
    line-height: 1;
    color: var(--holly-green);
    text-shadow: 3px 3px 0 var(--holly-green-dark);
    font-weight: 400;
  }
  .title-for {
    position: absolute;
    left: 340px;
    top: 348px;
    font-family: "Great Vibes", cursive;
    font-size: 64px;
    line-height: 1;
    color: var(--berry-red);
  }
  .title-drivers {
    position: absolute;
    left: 0;
    width: 838px;
    top: 415px;
    text-align: center;
    font-family: "Alfa Slab One", serif;
    font-size: 76px;
    line-height: 1;
    letter-spacing: 1px;
    color: var(--berry-red);
    font-weight: 400;
  }
  .title-drivers .cap { font-size: 92px; }
</style>
</head>
<body>
<main class="canvas">
  <section class="category-card category-card--electronics">
    <div class="gift-artwork" role="img" aria-label="Open red gift box with a gold bow holding a trucker headset and a GPS navigation device"></div>
    <div class="category-tag"><span>Electronics</span></div>
    <h1 class="campaign-title">
      <span class="title-gifts">Gifts</span>
      <span class="title-for">for</span>
      <span class="title-drivers"><span class="cap">T</span>RUCK <span class="cap">D</span>RIVERS</span>
    </h1>
  </section>

  <section class="category-card category-card--stockings">
    <div class="gift-artwork" role="img" aria-label="Open red gift box with a gold bow holding red and green Christmas stockings"></div>
    <div class="category-tag"><span>Stocking Stuffers</span></div>
    <h2 class="campaign-title">
      <span class="title-gifts">Gifts</span>
      <span class="title-for">for</span>
      <span class="title-drivers"><span class="cap">T</span>RUCK <span class="cap">D</span>RIVERS</span>
    </h2>
  </section>
</main>
</body>
</html>
```